https://velormark.com

We need a cool technology design for our Managed IT Services company. We are located in Coral Springs Florida. We provide all IT services and support for small to medium sized businesses. We would like to see designs that use our blue and white colors from our website.

```html
<!DOCTYPE html>
<html lang="en">
<head>
<meta charset="utf-8">
<title>Velormark Business Card</title>
<link href="https://fonts.googleapis.com/css2?family=Roboto+Condensed:wght@400;700&display=swap" rel="stylesheet">
<style>
  :root {
    --navy: #1b3461;
    --navy-deep: #132849;
    --white: #ffffff;
    --silver: #d9dde3;
    --silver-soft: #eceef1;
    --stage: #e9ebee;
  }
  html, body {
    margin: 0;
    padding: 0;
    width: 1200px;
    height: 896px;
    overflow: hidden;
    background: var(--stage);
    font-family: "Roboto Condensed", sans-serif;
  }
  .canvas {
    position: relative;
    width: 1200px;
    height: 896px;
    display: flex;
    align-items: center;
    justify-content: center;
    gap: 40px;
  }
  .card {
    position: relative;
    width: 540px;
    height: 310px;
    border-radius: 18px;
    overflow: hidden;
    box-shadow: 0 10px 28px rgba(19, 40, 73, 0.22);
  }
  /* Front side */
  .card-front {
    background: linear-gradient(150deg, #24427a 0%, var(--navy) 45%, var(--navy-deep) 100%);
    color: var(--white);
  }
  .world-map {
    position: absolute;
    left: 60px;
    top: 40px;
    width: 420px;
    height: 220px;
    border-radius: 50%;
    background: radial-gradient(ellipse at center, rgba(255,255,255,0.10) 0%, rgba(255,255,255,0.03) 60%, rgba(255,255,255,0) 75%);
  }
  .front-brand {
    position: absolute;
    left: 0;
    right: 0;
    top: 118px;
    display: flex;
    align-items: center;
    justify-content: center;
    gap: 14px;
  }
  .brand-dot {
    width: 22px;
    height: 22px;
    border-radius: 50%;
    background: var(--white);
  }
  .front-brand .brand-name {
    font-size: 52px;
    font-weight: 700;
    letter-spacing: 1px;
    color: var(--white);
  }
  .front-url {
    position: absolute;
    right: 40px;
    bottom: 30px;
    font-size: 14px;
    color: var(--white);
  }
  /* Back side */
  .card-back {
    background: var(--white);
  }
  .card-back svg.waves {
    position: absolute;
    inset: 0;
  }
  .back-brand {
    position: absolute;
    left: 40px;
    top: 172px;
    display: flex;
    align-items: center;
    gap: 10px;
  }
  .back-brand .brand-dot {
    width: 14px;
    height: 14px;
    background: var(--navy);
  }
  .back-brand .brand-name {
    font-size: 34px;
    font-weight: 700;
    color: var(--navy);
    letter-spacing: 0.5px;
  }
  .holder {
    position: absolute;
    right: 150px;
    top: 26px;
    text-align: right;
    color: var(--navy);
  }
  .holder-name {
    font-size: 22px;
    font-weight: 700;
    letter-spacing: 0.5px;
  }
  .holder-title {
    font-size: 13px;
  }
  .contact {
    position: absolute;
    right: 22px;
    top: 116px;
    list-style: none;
    margin: 0;
    padding: 0;
    color: var(--white);
    font-size: 14px;
    line-height: 23px;
    text-align: right;
  }
  .contact li {
    display: flex;
    justify-content: flex-end;
    align-items: center;
    gap: 8px;
  }
  .contact .icon {
    width: 12px;
    height: 12px;
    flex: none;
  }
  .contact .no-icon {
    padding-right: 20px;
  }
  .contact .address-start {
    margin-top: 10px;
  }
</style>
</head>
<body>
<main class="canvas">
  <section class="card card-front">
    <div class="world-map" role="img" aria-label="Faint dotted world map in the background"></div>
    <div class="front-brand">
      <span class="brand-dot"></span>
      <span class="brand-name">VELORMARK</span>
    </div>
    <div class="front-url">www.velormark.com</div>
  </section>

  <section class="card card-back">
    <svg class="waves" width="540" height="310" viewBox="0 0 540 310" aria-hidden="true">
      <path d="M400,0 C340,90 320,210 70,310 L540,310 L540,0 Z" fill="var(--silver-soft)"/>
      <path d="M420,0 C360,100 340,220 110,310 L540,310 L540,0 Z" fill="var(--silver)"/>
      <path d="M445,0 C385,110 370,230 160,310 L540,310 L540,0 Z" fill="var(--navy)"/>
    </svg>

    <div class="back-brand">
      <span class="brand-dot"></span>
      <span class="brand-name">VELORMARK</span>
    </div>

    <div class="holder">
      <div class="holder-name">DANIEL REYES</div>
      <div class="holder-title">Director</div>
    </div>

    <ul class="contact">
      <li>(555) 284-0148
        <svg class="icon" viewBox="0 0 12 12"><path d="M3,1 L5,3.5 L4,4.8 C4.8,6.4 5.6,7.2 7.2,8 L8.5,7 L11,9 L10,11 C5.5,10.5 1.5,6.5 1,2 Z" fill="none" stroke="var(--white)" stroke-width="1"/></svg>
      </li>
      <li>info@velormark.com
        <svg class="icon" viewBox="0 0 12 12"><rect x="1" y="2.5" width="10" height="7" fill="none" stroke="var(--white)" stroke-width="1"/><path d="M1,2.5 L6,6.5 L11,2.5" fill="none" stroke="var(--white)" stroke-width="1"/></svg>
      </li>
      <li>www.velormark.com
        <svg class="icon" viewBox="0 0 12 12"><circle cx="6" cy="6" r="5" fill="none" stroke="var(--white)" stroke-width="1"/><ellipse cx="6" cy="6" rx="2.2" ry="5" fill="none" stroke="var(--white)" stroke-width="0.8"/><line x1="1" y1="6" x2="11" y2="6" stroke="var(--white)" stroke-width="0.8"/></svg>
      </li>
      <li class="no-icon address-start">2750 Palm Grove Ave #110</li>
      <li class="no-icon">Harbor Glen, Ohio 45010</li>
    </ul>
  </section>
</main>
</body>
</html>
```